Finance Company Need Presentation Folder/ Brochure Design

We are a Finance Brokerage Firm in Adelaide, we provide finance for personal, car, equipment, boat and aviation loans. We are looking for designs for new presentation folders that are simplistic, yet professional and classy. We would like them to include the color orange and communicate financial safety and growth.

Target Market(s)

The folders will be going to current and perspective clients

Industry/Entity Type

Finance

Font styles to use
Other font styles liked:
• Raleway or something similar, example attached as 'Opening Keys Evening'

Colors
f37122
ffffff
000000

Requirements
Must have
• Phone Number: 1300 482 917
• Address:
• 47 Warrick Lane
• Brookhaven, SA 5071
• Website: tallowpeak.com.au
Nice to have
• "Experience finance in a whole new way... Experience Tallowpeak"
• Asset Finance - Home Loans - Personal Loans

```html
<!DOCTYPE html>
<html lang="en">
<head>
<meta charset="utf-8">
<title>Tallowpeak Presentation Folder</title>
<link href="https://fonts.googleapis.com/css2?family=Raleway:wght@400;500;700;800&display=swap" rel="stylesheet">
<style>
  :root {
    --orange: #f37122;
    --black: #0c0c0c;
    --cover-dark: #1b1718;
    --white: #ffffff;
    --grey-bg: #5b5b5b;
    --photo-light: #9a9a9a;
    --photo-mid: #5a5a5a;
    --photo-dark: #262626;
  }
  * { margin: 0; padding: 0; box-sizing: border-box; }
  html, body { width: 960px; height: 1200px; overflow: hidden; }
  body {
    background: var(--grey-bg);
    font-family: "Raleway", Arial, sans-serif;
    color: var(--white);
    display: flex;
    flex-direction: column;
    align-items: center;
    justify-content: space-evenly;
  }
  .spread { display: flex; width: 800px; height: 540px; box-shadow: 0 10px 30px rgba(0,0,0,.35); }
  .panel { position: relative; width: 400px; height: 540px; overflow: hidden; }

  /* Outer back */
  .back-cover { background: var(--cover-dark); }
  .back-cover .desk-photo {
    position: absolute; inset: 0;
    background: linear-gradient(160deg, #2a2526 0%, #1b1718 50%, #151213 100%);
  }
  .back-cover .brand {
    position: absolute; top: 200px; width: 100%;
    text-align: center; font-size: 34px; font-weight: 500; color: var(--white);
  }
  .contact-list {
    position: absolute; top: 268px; width: 100%;
    list-style: none; text-align: center; font-size: 12px; line-height: 1.45;
  }
  .contact-list li { margin-bottom: 12px; }
  .contact-list .dot {
    display: block; width: 6px; height: 6px; margin: 0 auto 3px;
    border-radius: 50%; background: var(--orange);
  }

  /* Outer front */
  .front-cover .road-photo {
    position: absolute; inset: 0;
    background: linear-gradient(180deg, #2b2b2b 0%, #4a4a4a 14%, var(--photo-light) 34%, var(--photo-mid) 52%, var(--photo-dark) 100%);
  }
  .front-cover .brand {
    position: absolute; top: 26px; width: 100%;
    text-align: center; font-size: 36px; font-weight: 500; color: var(--orange);
  }
  .headline {
    position: absolute; top: 112px; width: 100%;
    text-align: center; color: var(--black); font-weight: 800; line-height: 1.05;
  }
  .headline .line-1 { display: block; font-size: 19px; color: var(--white); }
  .headline .line-2 { display: block; font-size: 19px; }
  .headline .line-3 { display: block; font-size: 19px; color: var(--white); }
  .headline .services { display: block; margin-top: 4px; font-size: 9px; font-weight: 700; }
  .front-cover .website {
    position: absolute; bottom: 28px; right: 34px;
    font-size: 12px; letter-spacing: 2px; color: #d8d8d8;
  }

  /* Inside */
  .inside-left { background: var(--black); }
  .inside-left .fold-sheen {
    position: absolute; top: 0; right: 0; width: 90px; height: 100%;
    background: linear-gradient(90deg, rgba(0,0,0,0) 0%, rgba(255,255,255,.12) 60%, rgba(0,0,0,.3) 100%);
  }
  .inside-left .brand {
    position: absolute; top: 150px; width: 100%;
    text-align: center; font-size: 32px; font-weight: 500; color: var(--orange);
  }
  .inside-right { background: var(--black); }
  .inside-right svg { position: absolute; inset: 0; }
</style>
</head>
<body>

  <section class="spread outer-spread">
    <div class="panel back-cover">
      <div class="desk-photo" role="img" aria-label="Dim photo of a laptop and pen on a desk"></div>
      <div class="brand">Tallowpeak</div>
      <ul class="contact-list">
        <li><span class="dot"></span>1300 482 917</li>
        <li><span class="dot"></span>47 Warrick Lane<br>Brookhaven, SA 5071</li>
        <li><span class="dot"></span>admin@tallowpeak.com.au</li>
        <li><span class="dot"></span>www.tallowpeak.com.au</li>
      </ul>
    </div>
    <div class="panel front-cover">
      <div class="road-photo" role="img" aria-label="Black and white photo of an SUV driving on a country road under a cloudy sky"></div>
      <div class="brand">Tallowpeak</div>
      <p class="headline">
        <span class="line-1">EXPERIENCE FINANCE</span>
        <span class="line-2">in a whole new way...</span>
        <span class="line-3">Experience Tallowpeak</span>
        <span class="services">Asset Finance - Home Loans - Personal Loans</span>
      </p>
      <div class="website">www.tallowpeak.com.au</div>
    </div>
  </section>

  <section class="spread inside-spread">
    <div class="panel inside-left">
      <div class="brand">Tallowpeak</div>
      <div class="fold-sheen"></div>
    </div>
    <div class="panel inside-right">
      <svg width="400" height="540" viewBox="0 0 400 540" aria-hidden="true">
        <rect class="pocket" x="0" y="80" width="400" height="460" fill="#f37122"/>
        <path class="pocket-flap" d="M0 430 C20 370 60 350 120 350 L400 350 L400 540 L0 540 Z" fill="#0c0c0c"/>
      </svg>
    </div>
  </section>

</body>
</html>
```